Fernlake Business Card Design

We are looking for a fresh business card design for our new logo. We would like a business card that is unique but friendly. We are in the window coverings business offering blinds, shutters and shades for homes.

Target Market(s)

Targeting the end-consumer

Industry/Entity Type

Business

Requirements
Must have
• Must have a dedicates space for a photo of our sales person. Must contain our new logo (attached).

```html
<!DOCTYPE html>
<html lang="en">
<head>
<meta charset="utf-8">
<title>Fernlake Business Card</title>
<link rel="stylesheet" href="https://fonts.googleapis.com/css2?family=Ubuntu:wght@400;500;700&display=swap">
<style>
  :root {
    --leaf-green: #8bc443;
    --ink-grey: #6b6b6b;
    --paper-white: #ffffff;
    --backdrop: #ecebe8;
  }
  * { margin: 0; padding: 0; box-sizing: border-box; }
  html, body { width: 1200px; height: 663px; overflow: hidden; }
  body {
    background: var(--backdrop);
    font-family: "Ubuntu", sans-serif;
    position: relative;
  }
  .card {
    position: absolute;
    top: 181px;
    width: 520px;
    height: 300px;
    box-shadow: 0 6px 18px rgba(0,0,0,0.18);
    overflow: hidden;
  }
  /* Front */
  .card-front { left: 50px; background: var(--leaf-green); }
  .card-front .corner-lines { position: absolute; inset: 0; }
  .brand-lockup {
    position: absolute;
    left: 50%; top: 50%;
    transform: translate(-50%, -50%);
    display: flex; align-items: center; gap: 16px;
  }
  .brand-mark {
    width: 42px; height: 42px;
    border: 2px solid var(--ink-grey);
    border-radius: 4px;
  }
  .brand-name {
    font-size: 46px; font-weight: 400;
    color: var(--ink-grey);
    letter-spacing: 0.5px;
  }
  /* Back */
  .card-back { left: 630px; background: var(--paper-white); }
  .name-band {
    position: absolute;
    left: 0; top: 48px;
    width: 360px; height: 54px;
    background: var(--leaf-green);
    border-bottom: 2px solid var(--paper-white);
    box-shadow: 0 3px 0 0 var(--ink-grey);
  }
  .photo-slot {
    position: absolute; left: 74px; top: 12px;
    width: 28px; height: 28px;
    border: 1.5px solid var(--ink-grey);
  }
  .person-name {
    position: absolute; left: 116px; top: 10px;
    font-size: 17px; font-weight: 700;
    color: var(--paper-white); letter-spacing: 0.5px;
  }
  .person-title {
    position: absolute; left: 116px; top: 30px;
    font-size: 13px; font-weight: 400;
    color: var(--ink-grey); letter-spacing: 1px;
  }
  .brand-block {
    position: absolute;
    left: 372px; right: 0; top: 48px; height: 88px;
    background: var(--leaf-green);
    border: 2px solid var(--ink-grey);
    border-right: none;
    display: flex; align-items: center; justify-content: center;
  }
  .brand-block .brand-name-small {
    font-size: 22px; font-weight: 500;
    color: var(--paper-white);
  }
  .contact-list {
    position: absolute; left: 40px; top: 126px;
    list-style: none;
    font-size: 12.5px; line-height: 19px;
    color: var(--ink-grey);
  }
  .contact-list .email { font-weight: 700; }
</style>
</head>
<body>
  <section class="card card-front" aria-label="Card front">
    <svg class="corner-lines" width="520" height="300" viewBox="0 0 520 300">
      <polygon points="330,14 506,14 380,86" fill="none" stroke="var(--ink-grey)" stroke-width="1.5"/>
      <polygon points="506,214 506,286 334,286" fill="none" stroke="var(--ink-grey)" stroke-width="1.5"/>
    </svg>
    <div class="brand-lockup">
      <span class="brand-mark"></span>
      <span class="brand-name">Fernlake</span>
    </div>
  </section>

  <section class="card card-back" aria-label="Card back">
    <div class="name-band">
      <span class="photo-slot" role="img" aria-label="Space for salesperson photo"></span>
      <span class="person-name">DANA MORROW</span>
      <span class="person-title">CEO</span>
    </div>
    <div class="brand-block">
      <span class="brand-name-small">Fernlake</span>
    </div>
    <ul class="contact-list">
      <li>88 Elm Street Portland OR, 9720</li>
      <li class="email">hello@danamorrowfl.com</li>
      <li>+1 555 204 7731</li>
      <li>www.fernlake.com</li>
    </ul>
  </section>
</body>
</html>
```